Roofing & Siding door hanger flyer

-Looking to make door hanger flyer for Pellmont Roofing & Siding
-4.5" wide x 11" tall
-2 sided full colour
-We have started a new website (the content is changing) I have attached photos.
-About us:
-25 year labour warranty's available
-32 years in Calgary
-QCR A+ Member
-NWTG (Prairie Joint Shingle Guild) (logo attached)
-KOV Summit Select (logo attached)
-Owen Brisket (logo attached)
-Slogan "Raised On Care, Proven Through Seasons" 32 years in Calgary
-Sale
-Page 1 & 2 design ideas
We are in your area, contact us today for your Exclusive limited time offer! *discounts apply exclusively to new agreements only
Updates
-Please keep simple, clean & bright
-I really like the bright blue from our new logo (new logo uploaded)
-We specialize in Roofing -Siding-Gutters & full Exterior Renos (like the competitor example uploaded)
-This is the NEW website we are currently working on (not finished) https://mockview.example-draftpad.net/view/1a2b3c4d-5e6f-4a7b-8c9d-0e1f2a3b4c5d-7k2m/?fullscreen
-This is our OLD website https://pellmontshingleworks.com
-For the sale "We are in your area, contact us today for your Exclusive limited time offer" *discounts apply exclusively to new agreements only
-Free Estimates
-our phone# is 403-555-0148
-our website is pellmontshingleworks.com
-keep simple, clean, bright use the "new logo" uploaded. Check out the competitor example uploaded file
-We are in your area, Contact us today for your Exclusive limited time offer! *discounts apply to new agreements only
-FREE ESTIMATES
-Specialized in Roofing /Siding /Gutters Full Exterior Reno's
-We are currently working on a NEW website https://mockview.example-draftpad.net/view/1a2b3c4d-5e6f-4a7b-8c9d-0e1f2a3b4c5d-7k2m/?fullscreen
-Our OLD website https://pellmontshingleworks.com/
-Post old site address on flyer pellmontshingleworks.com
-Phone # 403-555-0148
Target Market(s)
40-55
Industry/Entity Type
Roofing Siding & full Exterior Reno's
Look and feel

```html
<!DOCTYPE html>
<html lang="en">
<head>
<meta charset="utf-8">
<title>Pellmont Roofing &amp; Siding – Door Hanger</title>
<link rel="stylesheet" href="https://fonts.googleapis.com/css2?family=Montserrat:wght@500;600;700;800&display=swap">
<style>
  :root{
    --stage:#8a8d90;
    --navy:#1d5192;
    --navy-dark:#174478;
    --bright-blue:#1f7fd8;
    --red:#e3151b;
    --white:#ffffff;
    --ink:#1a1a1a;
    --gold:#c9a23a;
  }
  *{box-sizing:border-box;margin:0;padding:0}
  html,body{width:1200px;height:1139px;overflow:hidden}
  body{
    background:var(--stage);
    font-family:"Montserrat",sans-serif;
    position:relative;
  }
  .hanger{
    position:absolute;top:70px;width:410px;height:1000px;
    border:12px solid var(--red);
    background:linear-gradient(160deg,var(--navy) 0%,var(--navy-dark) 100%);
    overflow:hidden;
    box-shadow:0 14px 30px rgba(0,0,0,.35);
  }
  .hanger--front{left:150px}
  .hanger--back{left:640px}
  .hanger__hole{
    position:absolute;top:50px;left:50%;width:128px;height:128px;margin-left:-64px;
    border-radius:50%;background:var(--white);z-index:3;
    box-shadow:inset 0 2px 6px rgba(0,0,0,.2);
  }
  .white-band{position:absolute;left:0;right:0;background:var(--white)}
  .brand{
    display:flex;align-items:center;gap:8px;
    font-weight:700;color:var(--navy);text-transform:uppercase;letter-spacing:.5px;
  }
  .brand__mark{width:14px;height:14px;background:var(--bright-blue);flex:none}
  .tagline-red{color:var(--red);font-weight:800;text-transform:uppercase}

  /* front */
  .front-header{top:150px;height:225px}
  .front-header .brand{position:absolute;top:82px;left:0;right:0;justify-content:center;font-size:26px;line-height:1.15;text-align:center}
  .front-header .tagline-red{position:absolute;bottom:18px;left:0;right:0;text-align:center;font-size:17px}
  .photo{position:absolute;width:170px;height:150px;border-radius:14px;border:3px solid rgba(255,255,255,.85)}
  .photo--roof{left:18px;top:390px;background:linear-gradient(160deg,#7fa8d6 0%,#a4473f 50%,#9c948a 100%)}
  .photo--siding{right:18px;top:553px;background:linear-gradient(160deg,#d9dde2 0%,#4c5d74 45%,#2f3b4b 100%)}
  .photo--exterior{left:18px;top:716px;height:138px;background:linear-gradient(180deg,#9cc0e6 0%,#e8e9ea 45%,#6f8f4b 100%)}
  .service{position:absolute;color:var(--white);text-align:center;width:175px}
  .service__title{font-size:22px;font-weight:600;letter-spacing:.5px;text-transform:uppercase}
  .service__rule{width:50px;height:1px;background:rgba(255,255,255,.7);margin:7px auto 8px}
  .service__items{font-size:13px;font-weight:600;line-height:1.3}
  .service--roofing{right:12px;top:414px}
  .service--siding{left:10px;top:574px}
  .service--exteriors{right:8px;top:724px;width:185px}
  .service--exteriors .service__title{font-size:18px}
  .service--exteriors .service__items{font-size:12.5px;line-height:1.25}

  .call-band{bottom:0;height:110px;display:flex;flex-direction:column;justify-content:center;align-items:center;gap:4px}
  .call-band__phone{font-size:27px;font-weight:800;color:var(--navy)}
  .call-band__web{font-size:16px;font-weight:600;color:var(--ink);letter-spacing:.5px}
  .hanger--back .call-band__phone{color:var(--red)}

  /* back */
  .back-header{
    position:absolute;top:195px;left:14px;right:14px;height:200px;
    background:var(--white);border:5px solid var(--bright-blue);outline:4px solid var(--white);
    display:flex;align-items:center;padding:0 12px;gap:12px;
  }
  .back-header .brand{width:130px;font-size:16px;line-height:1.2;flex:none}
  .back-header__divider{width:1px;align-self:stretch;margin:24px 0;background:#b8c3d0}
  .back-header__copy{text-align:center;flex:1}
  .slogan{font-size:17px;font-weight:700;color:var(--navy);line-height:1.25;margin-bottom:10px}
  .back-header .tagline-red{font-size:14px;line-height:1.2}
  .facts{position:absolute;top:420px;left:0;right:0;color:var(--white);font-size:16px;font-weight:600;text-align:center;line-height:1.45}
  .facts li{list-style:none;display:flex;align-items:center;justify-content:center;gap:7px}
  .facts li::before{content:"";width:9px;height:9px;background:var(--red);border-radius:50%}
  .facts__rule{width:70px;height:1px;background:rgba(255,255,255,.7);margin:12px auto}
  .offer{color:var(--white);font-size:16.5px;font-weight:600;line-height:1.35;text-align:center}
  .badge{position:absolute;background:var(--white);border:2px solid #cfd8e3}
  .badge--guild-wide{left:26px;top:680px;width:150px;height:50px}
  .badge--guild-square{left:26px;top:745px;width:76px;height:76px}
  .badge--anniversary{left:190px;top:682px;width:72px;height:72px;border-radius:50%;background:var(--gold);border:4px solid #1f5aa0}
  .badge--summit{left:124px;top:754px;width:64px;height:64px;background:#1f4f9a;border:3px solid var(--white);transform:rotate(45deg)}
  .badge--rating{left:280px;top:696px;width:94px;height:66px;background:#2c6fc2;border:3px solid var(--white)}
  .badge--maker{left:210px;top:768px;width:60px;height:62px;background:var(--white)}
  .badge--maker::after{content:"";position:absolute;inset:8px;background:var(--red)}
  .badge--cladding{left:284px;top:776px;width:90px;height:54px}
  .estimates{
    position:absolute;left:36px;right:36px;top:838px;height:50px;z-index:4;
    background:var(--red);
    clip-path:polygon(0 50%,5% 10%,10% 30%,15% 0,20% 22%,26% 4%,32% 20%,40% 0,48% 18%,56% 2%,64% 20%,72% 0,80% 22%,86% 4%,91% 26%,95% 8%,100% 50%,95% 90%,91% 72%,86% 100%,80% 78%,72% 100%,64% 80%,56% 98%,48% 80%,40% 100%,32% 80%,26% 96%,20% 78%,15% 100%,10% 70%,5% 90%);
  }
  .estimates__inner{
    position:absolute;inset:3px 6px;
    background:var(--white);
    clip-path:inherit;
    display:flex;align-items:center;justify-content:center;
    font-size:19px;font-weight:600;color:var(--navy);letter-spacing:.5px;
  }
  .hanger--back .call-band{height:100px;padding-top:22px;gap:2px}
  .hanger--back .call-band__phone{font-size:26px}
</style>
</head>
<body>

<section class="hanger hanger--front" aria-label="Door hanger front">
  <div class="hanger__hole"></div>
  <header class="white-band front-header">
    <div class="brand"><span class="brand__mark"></span><span>Pellmont<br>Roofing &amp; Siding</span></div>
    <p class="tagline-red">We're in your neighbourhood!</p>
  </header>

  <div class="photo photo--roof" role="img" aria-label="Photo of a red and grey house with a new shingle roof"></div>
  <div class="service service--roofing">
    <h2 class="service__title">Roofing</h2>
    <div class="service__rule"></div>
    <p class="service__items">Asphadlt<br>Rubber<br>Metal</p>
  </div>

  <div class="service service--siding">
    <h2 class="service__title">Siding</h2>
    <div class="service__rule"></div>
    <p class="service__items">Brisket Fibre cement<br>Vinyl<br>Metal (Steel, Aluminum)<br>Longboard</p>
  </div>
  <div class="photo photo--siding" role="img" aria-label="Photo of a two-storey home with blue-grey siding"></div>

  <div class="photo photo--exterior" role="img" aria-label="Photo of a white house with a front lawn"></div>
  <div class="service service--exteriors">
    <h2 class="service__title">Full Exteriors</h2>
    <div class="service__rule"></div>
    <p class="service__items">Eavestrough / Soffit<br>Fascia ,Stucco<br>Stone ,Insulation<br>Skylights, Painting<br>Windows &amp; Doors<br>Shake Repairs</p>
  </div>

  <footer class="white-band call-band">
    <p class="call-band__phone">CALL : (403) 555 - 0148</p>
    <p class="call-band__web">www.pellmontshingleworks.com</p>
  </footer>
</section>

<section class="hanger hanger--back" aria-label="Door hanger back">
  <div class="hanger__hole"></div>
  <header class="back-header">
    <div class="brand"><span class="brand__mark"></span><span>Pellmont Roofing &amp; Siding</span></div>
    <div class="back-header__divider"></div>
    <div class="back-header__copy">
      <p class="slogan">"Raised On Care,<br>Proven Through Seasons"</p>
      <p class="tagline-red">We're in your<br>neighbourhood!</p>
    </div>
  </header>

  <div class="facts">
    <ul>
      <li>25 year labour warranty's</li>
      <li>32 years in Calgary</li>
    </ul>
    <div class="facts__rule"></div>
    <p class="offer">"We are in your area,<br>contact us today for your<br>Exclusive limited time offer"<br>*discounts apply exclusively<br>to new agreements only</p>
  </div>

  <div class="badge badge--guild-wide" role="img" aria-label="Prairie Joint Shingle Guild member badge"></div>
  <div class="badge badge--guild-square" role="img" aria-label="Prairie Joint Shingle Guild badge"></div>
  <div class="badge badge--anniversary" role="img" aria-label="32nd anniversary seal"></div>
  <div class="badge badge--summit" role="img" aria-label="KOV Summit Select contractor badge"></div>
  <div class="badge badge--rating" role="img" aria-label="QCR A+ rating badge"></div>
  <div class="badge badge--maker" role="img" aria-label="Shingle manufacturer badge"></div>
  <div class="badge badge--cladding" role="img" aria-label="Owen Brisket siding badge"></div>

  <div class="estimates"><div class="estimates__inner">FREE ESTIMATES</div></div>

  <footer class="white-band call-band">
    <p class="call-band__phone">CALL : (403) 555 - 0148</p>
    <p class="call-band__web">www.pellmontshingleworks.com</p>
  </footer>
</section>

</body>
</html>
```